Freelance film producer/editor wants you to brisk vanta!

'Brisk Vanta' is my production business based in Melbourne, though I do a fair bit of work overseas. I'm a one woman show most of the time but enlist other crew members for larger projects. I manage productions from start to finish including producing, filming, editing, distribution, photography and animation.

My current tag line and details are as follows:

Greta Hollensby
Producer. Editor. Thinker.
[M] +61 417 562 093
[E] gh[at]briskvanta.com.au
www.briskvanta.com.au

I have a fairly wicked sense of humour and love a good pun, so feel free to work this into your design!

The final designs should demonstrate the areas I work in but not limited to. I'd rather not use old and typical "film" looking elements such as a clapper or negative reel. Having said that, the logo itself (attached) is quite typical because the first 'o' is a closed aperture and the second is a wide aperture. Happy for the logo to be pulled apart for the business card to be more interesting.

The majority of projects I work on are quite different and in some cases a bit crazy. Lots of travel involved. The main difference between me and other producers is that I don't say I work in 'film', even though i do. I want the card to leave me open to new roles and projects as opposed to squashing myself into one particular category.

I'm open to colour but prefer a simple design that isn't too hectic.

I have also attached an example I did like that was printed on plastic but then I realised so many other people had ripped it off....

I'm open to paper board or plastic (transparent) designs etc. One sided or two sided.

Thanks for sharing your ideas with me and please, go as nuts as you want to with this! :)

Target Market(s)

My clients range from non profits in health and educational institutions to record labels and well known artists. The business attracts corporates as well though the majority of my business is achieved through referral and word of mouth so most people will soon realise that my personality and work are very much intertwined and the reason they hire me for a job.

Industry/Entity Type

Business

Font styles to use
Other font styles liked:
• Eurostile or similar

Requirements
Must have
• I have a very open mind when it comes to design. I do like the existing tag line but if you can come up with something better I'm all ears! (and eyes)

Nice to have
• Back of the business card can be graphics, there can be transparent elements or holes, embossing options...
Should not have
• Besides my name, nothing should scream "I am woman!" because in my industry that's not a selling point.

The colour pink is a definite no.

```html
<!DOCTYPE html>
<html lang="en">
<head>
<meta charset="utf-8">
<title>Brisk Vanta — Business Card</title>
<link href="https://fonts.googleapis.com/css2?family=Open+Sans:wght@300;400;600&display=swap" rel="stylesheet">
<style>
  :root {
    --backdrop: #3b4a66;
    --card: #0e0e0f;
    --card-edge: #1c1c1e;
    --ink: #f4f4f4;
    --ink-soft: #d8d8d8;
  }
  * { margin: 0; padding: 0; box-sizing: border-box; }
  html, body {
    width: 1200px;
    height: 1000px;
    overflow: hidden;
    background: var(--backdrop);
    font-family: "Open Sans", Arial, sans-serif;
  }
  .canvas {
    position: relative;
    width: 1200px;
    height: 1000px;
  }
  .card {
    position: absolute;
    width: 580px;
    height: 340px;
    background: radial-gradient(ellipse at 40% 35%, var(--card-edge), var(--card) 70%);
    color: var(--ink);
    box-shadow: 0 10px 30px rgba(0, 0, 0, 0.35);
  }
  .card--front { left: 560px; top: 110px; }
  .card--back  { left: 70px;  top: 540px; }

  .brand {
    position: absolute;
    left: 0; right: 0; top: 128px;
    text-align: center;
  }
  .brand__name {
    display: inline-flex;
    align-items: center;
    gap: 14px;
    font-weight: 300;
    font-size: 50px;
    letter-spacing: 1px;
    line-height: 1;
    color: var(--ink);
  }
  .brand__dot {
    width: 34px; height: 34px;
    border-radius: 50%;
    background: var(--ink);
  }
  .brand__tagline {
    margin-top: 12px;
    font-size: 14px;
    letter-spacing: 1px;
    color: var(--ink-soft);
  }

  .contact {
    position: absolute;
    left: 150px;
    top: 120px;
    width: 330px;
    text-align: center;
  }
  .contact__name {
    font-weight: 600;
    font-size: 22px;
    line-height: 1.05;
  }
  .contact__role {
    font-size: 17px;
    color: var(--ink-soft);
    margin-bottom: 22px;
  }
  .contact__line {
    font-size: 20px;
    line-height: 1.35;
    white-space: pre;
  }
</style>
</head>
<body>
  <main class="canvas">
    <section class="card card--front" aria-label="Card front">
      <div class="brand">
        <div class="brand__name"><span>brisk vanta</span><span class="brand__dot"></span></div>
        <p class="brand__tagline">Poducer. Editor.Thinker.</p>
      </div>
    </section>

    <section class="card card--back" aria-label="Card back">
      <div class="contact">
        <p class="contact__name">Greta Hollensby</p>
        <p class="contact__role">Owner</p>
        <p class="contact__line">Tel: +61 417   562 093</p>
        <p class="contact__line">Email: gh@briskvanta.com.au</p>
        <p class="contact__line">Website: www.briskvanta.com.au</p>
      </div>
    </section>
  </main>
</body>
</html>
```